I am planning to launch a new online company called allphonedeskhub.net. This will be a place where people who work in call centres can come and purchase downloadable templates, tool-kits, courseware etc to help them in their jobs. The site will also share the latest information around research, best practices, news in the industry. Essentially a hub for Allphonedesk Hub related.

I need someone to build the site for me from scratch (I have only just bought the domain name). Everything from the look and feel of the website (focus on easy to use, clean and sharp graphics, with a bit of fun), highly focused on social media and building a community, full blown e-commerce that allows for memberships/subscriptions/and one off purchase models. If you can also design custom graphics (high quality) that would be even better. Given my research of other companies in this space their websites are very dull that look like knowledge bases. I will want alot of cool visuals that attract the customers in. My initial thinking on colour scheme is bright greens/pinks/yellows etc. Not fluorescent though!

The site will contain alot of documents, templates, presentations, videos, articles, white papers etc. You must have experience in the best way to structure the site in an organised manner so that my customer can find what they need very easily.

The person who takes on this work must be happy to work collaboratively with me. It is also key that when the project is delivered that I am able to maintain alot of it myself in terms of uploading documents, blog updates, adding new products, real-time reports/analytics etc.

Whilst you are designing the website I will be working on the content so I will need your help to understand how I structure my content so that it makes sense for the design.

I will base my choice of designer on levels of experience (I will want to see previous work that you have done). I am not adverse to you using tools like shopify etc. if it meets the overall requirements of the site and adds to the functionality/look and feel.

Target Market(s)

People who work in call centres primarily those that are responsible for managing teams of the call centre itself

Industry/Entity Type

Business

Number of Pages Required

5+ page

Font styles to use
Sans Serif

Colors
33b8a4
34a6d7
886aae
b868aa
e667a6
f04a51
f68e4e
faa54b
ffcf3e

Requirements
Must have
• E-commerce functionality that allows for subscriptions and one-off payments
• Credit card processing and accept wire/bank transfers
• Easy to use layout
• Products sold alone and/or as part of bundles
• Membership area
• Front page
• About Us page
• Contact Us page
• Store page (with e-commerce back end)
• News page
• Free Resources page
• Cool, bright, fun look and feel
Nice to have
• Cool, bright, fun graphics
Should not have
• Should not look old fashioned or be difficult to navigate
• Should not look too busy or disorganised

```html
<!DOCTYPE html>
<html lang="en">
<head>
<meta charset="utf-8">
<title>Allphonedesk Hub – Call Centre Resources</title>
<link rel="stylesheet" href="https://fonts.googleapis.com/css2?family=Dosis:wght@400;500;600;700&family=Fjalla+One&display=swap">
<style>
:root{
  --teal:#33b8a4;--blue:#34a6d7;--purple:#886aae;--plum:#b868aa;--pink:#e667a6;
  --red:#f04a51;--orange:#f68e4e;--amber:#faa54b;--yellow:#ffcf3e;
  --ink:#333a40;--muted:#8a8f94;--line:#e4e4e4;--soft:#f4f4f4;--page:#fafafa;
  --green:#18845f;--green-light:#2fa27a;--deep:#1d5a6c;--slate:#5b6268;--foot:#ececec;
}
*{box-sizing:border-box;margin:0;padding:0}
html,body{width:1200px;height:2953px;overflow:hidden}
body{background:var(--page);font-family:"Dosis",sans-serif;color:var(--ink);font-size:13px}
.page{width:1200px;height:2953px;position:relative;overflow:hidden}
.wrap{width:858px;margin:0 auto;position:relative}
svg{display:block}
.defs{position:absolute;width:0;height:0}

/* header */
.topbar{height:100px;background:#fff;display:flex}
.brand{width:134px;height:100px;background:var(--red);color:#fff;padding:14px 12px;font-size:20px;font-weight:500;line-height:1.05}
.brand .dot{display:block;width:12px;height:12px;background:#fff;margin-top:6px}
.info{flex:1;position:relative}
.acct{position:absolute;right:0;top:0;display:flex;gap:14px;font-size:9px;font-weight:600;color:var(--red);letter-spacing:.5px}
.acct span{padding:4px 2px;border-bottom:1px solid var(--line)}
.info-items{display:flex;position:absolute;top:40px;left:14px;gap:28px}
.info-item{display:flex;align-items:center;gap:8px;font-size:10px;line-height:1.2;color:var(--muted);width:150px}
.info-item b{color:var(--ink);font-weight:500;display:block}
.ico{width:30px;height:30px;border:1px solid var(--line);border-radius:50%;display:flex;align-items:center;justify-content:center;flex:none}
.nav{height:38px;background:var(--red);display:flex;align-items:center}
.nav a{color:#fff;text-decoration:none;font-size:12px;padding:0 20px}
.search{margin-left:auto;width:130px;height:38px;background:#e03c43;color:#fff;font-size:11px;display:flex;align-items:center;justify-content:space-between;padding:0 12px}

/* hero */
.hero-row{display:flex;margin-top:4px;height:385px}
.categories{width:269px;background:var(--pink)}
.categories h3{height:36px;background:#fff;border-left:5px solid var(--yellow);color:var(--muted);font-size:14px;font-weight:600;padding:9px 12px;letter-spacing:.5px}
.categories li{list-style:none;height:38.8px;border-bottom:1px solid rgba(255,255,255,.5);color:#fff;font-size:11px;padding:12px 18px}
.hero{flex:1;background:var(--green);position:relative;overflow:hidden}
.hero-art{position:absolute;right:0;top:0;width:250px;height:385px;
  background:radial-gradient(ellipse 140px 150px at 62% 78%,rgba(255,255,255,.92),rgba(255,255,255,.35) 60%,rgba(255,255,255,0) 100%),
             radial-gradient(ellipse 160px 230px at 100% 40%,var(--green-light),rgba(47,162,122,0) 100%)}
.hero-copy{position:absolute;left:38px;top:176px;color:#fff;z-index:1}
.hero h1{font-family:"Fjalla One",sans-serif;font-weight:400;font-size:31px;letter-spacing:.5px;line-height:1.1}
.hero p{font-size:19px;letter-spacing:1px;margin-top:4px}

/* tiles */
.tiles{display:flex;gap:8px;margin-top:6px;height:300px}
.tile{flex:1;position:relative;overflow:hidden;color:#fff}
.tile-voice{background:var(--slate);text-align:center;padding-top:14px}
.tile-voice .q{font-size:15px;line-height:1.25}
.tile-voice .q em{font-style:normal;color:var(--yellow);font-size:22px;display:block}
.tile-voice .art{position:absolute;left:16px;right:16px;top:150px;height:110px;background:radial-gradient(ellipse at 50% 30%,#9aa1a7,#6d7379 75%)}
.tile-voice .cap{position:absolute;bottom:8px;width:100%;color:var(--yellow);font-size:16px}
.stack{display:flex;flex-direction:column;gap:6px;flex:1}
.tile-coach{flex:1;background:var(--teal)}
.tile-coach .art{height:118px;background:linear-gradient(160deg,#7fd0ee 0%,#3fa7d1 55%,#2c5f7a 100%)}
.tile-coach .cap{height:26px;background:#24313b;font-size:13px;padding:4px 10px}
.tile-free{flex:1;background:var(--blue);text-align:center;padding-top:16px}
.tile-free h4{font-weight:400;font-size:20px}
.btn-pill{display:inline-block;background:var(--pink);color:#fff;font-size:11px;padding:3px 12px;border-radius:2px;margin-top:4px}
.tile-free .art{position:absolute;bottom:0;left:0;right:0;height:52px;background:linear-gradient(rgba(52,166,215,0),#1f5f80)}
.tile-lead{background:var(--yellow);text-align:center;padding-top:8px}
.tile-lead h4{font-family:"Fjalla One",sans-serif;font-weight:400;font-size:22px;line-height:1.1;color:#fff}
.tile-lead .btn-pill{background:var(--blue)}
.tile-lead .art{position:absolute;left:14px;right:14px;bottom:10px;height:180px;background:radial-gradient(ellipse 70% 90% at 50% 100%,#2f8f86,#4fa99a 45%,rgba(255,207,62,0) 100%)}
.tile-social{background:var(--deep);padding:14px 10px}
.tile-social h4{font-size:18px;font-weight:600;letter-spacing:.5px;border-bottom:1px solid rgba(255,255,255,.25);padding-bottom:8px}
.tile-social .lbl{font-size:10px;margin:12px 0 6px;letter-spacing:.3px}
.sub{display:flex;height:22px;font-size:9px}
.sub span{flex:1;background:#2f7387;padding:5px 6px}
.sub b{background:var(--yellow);color:var(--ink);padding:5px 6px;font-weight:600}
.circles{display:grid;grid-template-columns:repeat(4,30px);gap:12px 18px;margin:20px 0 0 22px}
.circles i{width:30px;height:30px;border-radius:50%;border:2px solid #fff;display:block}
.member{position:absolute;left:10px;right:10px;bottom:22px;height:30px;background:var(--yellow);color:var(--ink);font-weight:700;font-size:12px;text-align:center;padding-top:7px}

/* product shelves */
.shelf{margin-top:34px}
.shelf + .shelf{margin-top:31px}
.shelf-head{height:33px;border-bottom:2px solid var(--ink);display:flex;align-items:flex-end;position:relative}
.tab{background:var(--pink);color:#fff;font-size:12px;font-weight:600;letter-spacing:.6px;padding:8px 20px;height:33px;border-left:4px solid var(--plum)}
.tab.plain{background:#fff;color:var(--ink);border:1px solid var(--line);border-bottom:none;margin-left:6px;font-weight:500}
.arrows{position:absolute;right:0;top:6px;display:flex;gap:2px}
.arrows i{width:14px;height:14px;background:var(--blue);display:flex;align-items:center;justify-content:center}
.cards{display:flex;gap:13px;margin-top:11px}
.card{width:204px;height:289px;background:#fff;border:1px solid var(--line);position:relative}
.thumb{margin:10px 10px 0;height:170px;position:relative}
.thumb .play{position:absolute;left:50%;top:50%;width:36px;height:36px;margin:-18px 0 0 -18px}
.card .meta{display:flex;justify-content:space-between;padding:16px 10px 0;font-size:12px}
.card .meta b{color:var(--red);font-weight:600}
.stars{color:var(--amber);font-size:9px;letter-spacing:1px;padding:4px 10px 0}
.actions{position:absolute;left:0;right:0;bottom:0;height:30px;display:flex}
.actions .cta{width:142px;background:var(--red);color:#fff;font-size:10px;font-weight:600;display:flex;align-items:center;gap:6px;padding-left:10px}
.actions .icn{flex:1;border-top:1px solid var(--line);border-left:1px solid var(--line);display:flex;align-items:center;justify-content:center}

/* news */
.news-box{margin-top:28px;height:313px;background:#fff;border:1px solid var(--line);display:flex;padding:18px 20px}
.news{width:530px;position:relative}
.news .shelf-head{border-bottom:1px solid var(--ink)}
.news .arrows{top:14px}
.post{display:flex;gap:10px;margin-top:12px;height:92px}
.post .pic{width:208px;height:92px;flex:none}
.post h5{font-size:13px;font-weight:500;border-bottom:1px solid var(--line);padding-bottom:8px}
.post p{font-size:11px;color:var(--muted);line-height:1.35;margin-top:6px}
.about{margin-left:40px;flex:1;border-left:1px solid var(--line);padding-left:14px}
.about h4{font-size:15px;font-weight:500;border-bottom:1px solid var(--line);padding-bottom:8px}
.about .name{font-size:15px;color:var(--muted);margin-top:14px;line-height:1.1}
.about p{font-size:11px;color:var(--muted);line-height:1.4;margin-top:22px}
.more{display:inline-block;background:var(--red);color:#fff;font-size:10px;padding:3px 12px;margin-top:12px}

/* footer */
.footer{position:absolute;left:0;top:2660px;width:1200px;height:293px;background:var(--foot)}
.foot-cols{display:flex;width:858px;margin:0 auto;padding-top:30px}
.foot-col h4{font-size:15px;font-weight:500;letter-spacing:.4px;margin-bottom:14px}
.qc{width:312px;padding-left:12px}
.field{width:236px;height:22px;background:#c9c9cf;font-size:10px;color:#fff;padding:4px 8px;margin-bottom:10px}
.field.area{height:58px}
.send{margin-left:186px;width:50px;height:16px;background:#3a2b3f;color:#fff;font-size:9px;text-align:center;padding-top:2px}
.rc{width:273px}
.comment{display:flex;gap:10px;margin-bottom:16px;font-size:11px;line-height:1.35}
.avatar{width:40px;height:40px;border-radius:50%;background:#d8d3dc;border:2px solid #fff;flex:none}
.comment b{color:var(--purple);font-weight:500}
.contact p{display:flex;gap:10px;font-size:11px;line-height:1.35;color:#555;margin-bottom:12px}
.squares{display:flex;gap:4px;margin-top:6px}
.squares i{width:18px;height:18px;border:1px solid #777;display:block}
.copy{position:absolute;left:173px;right:173px;top:240px;border-top:1px solid #d9d9d9;text-align:center;font-size:10px;color:#666;padding-top:20px}
</style>
</head>
<body>
<svg class="defs" aria-hidden="true">
  <symbol id="i-cart" viewBox="0 0 15 13"><path d="M0 1h3l2 7h8l2-5H4" fill="none" stroke="currentColor" stroke-width="1.6"/><circle cx="6" cy="11" r="1.3" fill="currentColor"/><circle cx="12" cy="11" r="1.3" fill="currentColor"/></symbol>
  <symbol id="i-cloud" viewBox="0 0 14 10"><path d="M3 9a3 3 0 010-6 4 4 0 017 0 3 3 0 011 6z" fill="#999"/></symbol>
  <symbol id="i-link" viewBox="0 0 11 11"><path d="M4 7l3-3M3 5L1 7a2 2 0 003 3l2-2M8 6l2-2a2 2 0 00-3-3L5 3" fill="none" stroke="#999" stroke-width="1.3"/></symbol>
  <symbol id="i-eye" viewBox="0 0 12 8"><path d="M0 4q6-7 12 0-6 7-12 0z" fill="#fff"/><circle cx="6" cy="4" r="1.6" fill="#f04a51"/></symbol>
  <symbol id="i-play" viewBox="0 0 36 36"><circle cx="18" cy="18" r="17" fill="rgba(0,0,0,.45)"/><path d="M14 11l11 7-11 7z" fill="#fff"/></symbol>
  <symbol id="i-prev" viewBox="0 0 6 8"><path d="M5 0L1 4l4 4" fill="#fff"/></symbol>
  <symbol id="i-next" viewBox="0 0 6 8"><path d="M1 0l4 4-4 4" fill="#fff"/></symbol>
</svg>
<div class="page">

<header class="wrap">
  <div class="topbar">
    <div class="brand">Allphonedesk<br>Hub<span class="dot"></span></div>
    <div class="info">
      <div class="acct"><span>REGISTER ▾</span><span>LOGIN ▾</span><span>MY ACCOUNT ▾</span></div>
      <div class="info-items">
        <div class="info-item"><span class="ico"><svg width="14" height="10" viewBox="0 0 14 10"><rect x="0.5" y="0.5" width="13" height="9" fill="none" stroke="#34a6d7"/><path d="M1 1l6 5 6-5" fill="none" stroke="#34a6d7"/></svg></span><span><b>info@allphonedeskhub.net</b>MAIL US</span></div>
        <div class="info-item"><span class="ico"><svg width="14" height="14" viewBox="0 0 14 14"><path d="M1 7l6-6h6v6l-6 6z" fill="#34a6d7"/><circle cx="10" cy="4" r="1.3" fill="#fff"/></svg></span><span><b>LATEST</b>SPECIAL OFFER</span></div>
        <div class="info-item"><span class="ico"><svg width="14" height="14" viewBox="0 0 14 14"><path d="M3 1l3 3-2 2c1 2 2 3 4 4l2-2 3 3-2 3C6 13 1 8 0 3z" fill="#34a6d7"/></svg></span><span><b>+44 555 0142</b>CALL US</span></div>
        <div class="info-item"><span class="ico"><svg width="15" height="13" style="color:#34a6d7"><use href="#i-cart"/></svg></span><span><b>$0.00 - 0 ITEM</b>YOUR CART</span></div>
      </div>
    </div>
  </div>
  <nav class="nav">
    <a>About Us</a><a>News</a><a>Free Stuff</a><a>Membership</a><a>Contact Us</a>
    <div class="search">Search <svg width="12" height="12" viewBox="0 0 12 12"><circle cx="5" cy="5" r="3.8" fill="none" stroke="#fff" stroke-width="1.6"/><path d="M8 8l3 3" stroke="#fff" stroke-width="1.8"/></svg></div>
  </nav>
</header>

<main class="wrap">
  <section class="hero-row">
    <aside class="categories">
      <h3>CATEGORIES</h3>
      <ul>
        <li>Performance Measurement &amp; Management</li><li>Morale and Motivation</li><li>Coaching and Mentoring</li>
        <li>Leadership and Management</li><li>Reward and Recognition</li><li>Communication Skills</li>
        <li>Call Centre Technology</li><li>Call Centre Strategy</li><li>Research and Best Practices</li>
      </ul>
    </aside>
    <div class="hero">
      <div class="hero-art" role="img" aria-label="Illustration of a smiling call centre agent with headset at a desk, surrounded by service icons"></div>
      <div class="hero-copy">
        <h1>Complete Call Centre</h1>
        <p>Services your business need</p>
      </div>
    </div>
  </section>

  <section class="tiles">
    <div class="tile tile-voice">
      <div class="q">Do you fully<em>Understand</em>The Voice<br>of your<em>Customers?</em></div>
      <div class="art" role="img" aria-label="Illustration of speech bubbles above a group of people"></div>
      <div class="cap">Communication Skills</div>
    </div>
    <div class="stack">
      <div class="tile tile-coach">
        <div class="art" role="img" aria-label="Illustration of an agent with headset at a computer"></div>
        <div class="cap">Coaching and Mentoring</div>
      </div>
      <div class="tile tile-free">
        <h4>Free Resources</h4>
        <span class="btn-pill">Download</span>
        <div class="art" role="img" aria-label="Illustration of raised hands"></div>
      </div>
    </div>
    <div class="tile tile-lead">
      <h4>Leadership and<br>Management</h4>
      <span class="btn-pill">More</span>
      <div class="art" role="img" aria-label="Illustration of figures arranged as rising arrows"></div>
    </div>
    <div class="tile tile-social">
      <h4>STAY IN TOUCH</h4>
      <div class="lbl">SUBSCRIBE TO OUR NEWSLETTER</div>
      <div class="sub"><span>enter your mail address</span><b>SUBSCRIBE</b></div>
      <div class="circles"><i></i><i></i><i></i><i></i><i></i><i></i><i></i><i></i></div>
      <div class="member">BECOME A MEMBER</div>
    </div>
  </section>

  <section class="shelf">
    <div class="shelf-head"><span class="tab">COURSEWARE</span>
      <div class="arrows"><i><svg width="6" height="8"><use href="#i-prev"/></svg></i><i><svg width="6" height="8"><use href="#i-next"/></svg></i></div></div>
    <div class="cards">
      <article class="card"><div class="thumb" role="img" aria-label="Course cover in yellow and red" style="background:radial-gradient(circle at 50% 45%,#ffe066,#ffc61e 50%,#f06a2f 100%)"></div><div class="meta"><span>Effective call...</span><b>$37.00</b></div><div class="stars">★★★★★</div>
        <div class="actions"><span class="cta"><svg width="12" height="10" style="color:#fff"><use href="#i-cart"/></svg>ADD TO CART</span><span class="icn"><svg width="14" height="10"><use href="#i-cloud"/></svg></span><span class="icn"><svg width="11" height="11"><use href="#i-link"/></svg></span></div></article>
      <article class="card"><div class="thumb" role="img" aria-label="Course cover with blue sky and an alarm clock" style="background:linear-gradient(#6fb9e3,#3c7fb5 60%,#2b4e73)"></div><div class="meta"><span>Wake up your...</span><b>$51.00</b></div><div class="stars">★★★★★</div>
        <div class="actions"><span class="cta"><svg width="12" height="10" style="color:#fff"><use href="#i-cart"/></svg>ADD TO CART</span><span class="icn"><svg width="14" height="10"><use href="#i-cloud"/></svg></span><span class="icn"><svg width="11" height="11"><use href="#i-link"/></svg></span></div></article>
      <article class="card"><div class="thumb" role="img" aria-label="Training handbook cover in black and orange" style="background:linear-gradient(#1e1e1e 0 30%,#f0a31e 30% 88%,#f7f2e6 88%)"></div><div class="meta"><span>Call centre Training...</span><b>$37.95</b></div><div class="stars">★★★★★</div>
        <div class="actions"><span class="cta"><svg width="12" height="10" style="color:#fff"><use href="#i-cart"/></svg>ADD TO CART</span><span class="icn"><svg width="14" height="10"><use href="#i-cloud"/></svg></span><span class="icn"><svg width="11" height="11"><use href="#i-link"/></svg></span></div></article>
      <article class="card"><div class="thumb" role="img" aria-label="Staffing book cover with headset agents above a yellow band" style="background:linear-gradient(#e9eef2,#d7dde2 66%,#ffcf3e 66%)"></div><div class="meta"><span>Call centre Staffing...</span><b>$249.93</b></div><div class="stars" style="color:#222">●●●●●</div>
        <div class="actions"><span class="cta"><svg width="12" height="10" style="color:#fff"><use href="#i-cart"/></svg>ADD TO CART</span><span class="icn"><svg width="14" height="10"><use href="#i-cloud"/></svg></span><span class="icn"><svg width="11" height="11"><use href="#i-link"/></svg></span></div></article>
    </div>
  </section>

  <section class="shelf">
    <div class="shelf-head"><span class="tab">VIDEOS</span>
      <div class="arrows"><i><svg width="6" height="8"><use href="#i-prev"/></svg></i><i><svg width="6" height="8"><use href="#i-next"/></svg></i></div></div>
    <div class="cards">
      <article class="card"><div class="thumb" role="img" aria-label="Black and white video still of a speaker" style="background:radial-gradient(circle at 40% 45%,#a9a9a9,#555 60%,#2a2a2a)"><svg class="play"><use href="#i-play"/></svg></div><div class="meta"><span>Inspirational speech</span><b>$12.00</b></div><div class="stars">★★★★★</div>
        <div class="actions"><span class="cta"><svg width="12" height="10" style="color:#fff"><use href="#i-cart"/></svg>ADD TO CART</span><span class="icn"><svg width="14" height="10"><use href="#i-cloud"/></svg></span><span class="icn"><svg width="11" height="11"><use href="#i-link"/></svg></span></div></article>
      <article class="card"><div class="thumb" role="img" aria-label="Video title card about improving first call resolution" style="background:linear-gradient(#fff 0 60%,#eef3f8 60% 80%,#f3e1e3 80%)"><svg class="play"><use href="#i-play"/></svg></div><div class="meta"><span>15 tips</span><b>$17.00</b></div><div class="stars">★★★★★</div>
        <div class="actions"><span class="cta"><svg width="12" height="10" style="color:#fff"><use href="#i-cart"/></svg>ADD TO CART</span><span class="icn"><svg width="14" height="10"><use href="#i-cloud"/></svg></span><span class="icn"><svg width="11" height="11"><use href="#i-link"/></svg></span></div></article>
      <article class="card"><div class="thumb" role="img" aria-label="Video still of an agent on a sales call" style="background:radial-gradient(circle at 55% 40%,#d9b48f,#9b7658 50%,#4f3e31)"><svg class="play"><use href="#i-play"/></svg></div><div class="meta"><span>Sales Call example</span><b>$11.95</b></div><div class="stars">★★★★★</div>
        <div class="actions"><span class="cta"><svg width="12" height="10" style="color:#fff"><use href="#i-cart"/></svg>ADD TO CART</span><span class="icn"><svg width="14" height="10"><use href="#i-cloud"/></svg></span><span class="icn"><svg width="11" height="11"><use href="#i-link"/></svg></span></div></article>
      <article class="card"><div class="thumb" role="img" aria-label="Video still of a hand writing a script on a whiteboard" style="background:linear-gradient(160deg,#fafafa,#e4e4e4 70%,#cfcfcf)"><svg class="play"><use href="#i-play"/></svg></div><div class="meta"><span>Cold Calling Script</span><b>$21.00</b></div><div class="stars">★★★★★</div>
        <div class="actions"><span class="cta"><svg width="12" height="10" style="color:#fff"><use href="#i-cart"/></svg>ADD TO CART</span><span class="icn"><svg width="14" height="10"><use href="#i-cloud"/></svg></span><span class="icn"><svg width="11" height="11"><use href="#i-link"/></svg></span></div></article>
    </div>
  </section>

  <section class="shelf">
    <div class="shelf-head"><span class="tab">PRESENTATION</span><span class="tab plain">TEMPLATES</span>
      <div class="arrows"><i><svg width="6" height="8"><use href="#i-prev"/></svg></i><i><svg width="6" height="8"><use href="#i-next"/></svg></i></div></div>
    <div class="cards">
      <article class="card"><div class="thumb" role="img" aria-label="Training slide deck preview in blue" style="background:linear-gradient(135deg,#3aa0dd,#1f6fb0 55%,#143e62)"></div><div class="meta"><span>Training PPT</span><b>$12.00</b></div><div class="stars">★★★★★</div>
        <div class="actions"><span class="cta"><svg width="12" height="10" style="color:#fff"><use href="#i-cart"/></svg>ADD TO CART</span><span class="icn"><svg width="14" height="10"><use href="#i-cloud"/></svg></span><span class="icn"><svg width="11" height="11"><use href="#i-link"/></svg></span></div></article>
      <article class="card"><div class="thumb" role="img" aria-label="Tips slide template in warm orange tones" style="background:radial-gradient(circle at 65% 40%,#fbe3c4,#f7b15c 55%,#ee8a2a)"></div><div class="meta"><span>Tips</span><b>$10.00</b></div><div class="stars">★★★★★</div>
        <div class="actions"><span class="cta"><svg width="12" height="10" style="color:#fff"><use href="#i-cart"/></svg>ADD TO CART</span><span class="icn"><svg width="14" height="10"><use href="#i-cloud"/></svg></span><span class="icn"><svg width="11" height="11"><use href="#i-link"/></svg></span></div></article>
      <article class="card"><div class="thumb" role="img" aria-label="Agent slide template with an office scene in blue" style="background:linear-gradient(#3f74ba,#6d9bd1 45%,#d5dee8)"></div><div class="meta"><span>Agent</span><b>$875.00</b></div><div class="stars">★★★★★</div>
        <div class="actions"><span class="cta"><svg width="12" height="10" style="color:#fff"><use href="#i-cart"/></svg>ADD TO CART</span><span class="icn"><svg width="14" height="10"><use href="#i-cloud"/></svg></span><span class="icn"><svg width="11" height="11"><use href="#i-link"/></svg></span></div></article>
      <article class="card"><div class="thumb" role="img" aria-label="Service slide template with a red figure at a laptop" style="background:radial-gradient(ellipse 45% 40% at 45% 45%,#e53935,#ef6b62 70%,#f2f2f2 100%)"></div><div class="meta"><span>Services</span><b>$150.00</b></div><div class="stars">★★★★★</div>
        <div class="actions"><span class="cta"><svg width="12" height="10" style="color:#fff"><use href="#i-cart"/></svg>ADD TO CART</span><span class="icn"><svg width="14" height="10"><use href="#i-cloud"/></svg></span><span class="icn"><svg width="11" height="11"><use href="#i-link"/></svg></span></div></article>
    </div>
  </section>

  <section class="shelf">
    <div class="shelf-head"><span class="tab">FREE RESOURCES</span>
      <div class="arrows"><i><svg width="6" height="8"><use href="#i-prev"/></svg></i><i><svg width="6" height="8"><use href="#i-next"/></svg></i></div></div>
    <div class="cards">
      <article class="card"><div class="thumb" role="img" aria-label="Dark blue graphic of connected software icons" style="background:radial-gradient(circle,#3a82bd,#17406a 55%,#0b2238)"><svg class="play"><use href="#i-play"/></svg></div><div class="meta"><span>software guidance (Video)</span></div><div class="stars">★★★★★</div>
        <div class="actions"><span class="cta"><svg width="12" height="8"><use href="#i-eye"/></svg>VIEW</span><span class="icn"><svg width="14" height="10"><use href="#i-cloud"/></svg></span><span class="icn"><svg width="11" height="11"><use href="#i-link"/></svg></span></div></article>
      <article class="card"><div class="thumb" role="img" aria-label="Document page introducing call centre training" style="background:linear-gradient(90deg,#f1c76b 0 8%,#fdfaf2 8%)"></div><div class="meta"><span>Tips</span></div><div class="stars">★★★★★</div>
        <div class="actions"><span class="cta"><svg width="12" height="8"><use href="#i-eye"/></svg>VIEW</span><span class="icn"><svg width="14" height="10"><use href="#i-cloud"/></svg></span><span class="icn"><svg width="11" height="11"><use href="#i-link"/></svg></span></div></article>
      <article class="card"><div class="thumb" role="img" aria-label="Illustration of office workers at desks" style="background:linear-gradient(#eef3f6,#c9d3da 55%,#8e9aa3)"></div><div class="meta"><span>Article</span></div><div class="stars">★★★★★</div>
        <div class="actions"><span class="cta"><svg width="12" height="8"><use href="#i-eye"/></svg>VIEW</span><span class="icn"><svg width="14" height="10"><use href="#i-cloud"/></svg></span><span class="icn"><svg width="11" height="11"><use href="#i-link"/></svg></span></div></article>
      <article class="card"><div class="thumb" role="img" aria-label="Blue white paper cover with a document graphic" style="background:linear-gradient(#34aee3,#2496cc)"></div><div class="meta"><span>White Paper</span></div><div class="stars">★★★★★</div>
        <div class="actions"><span class="cta"><svg width="12" height="8"><use href="#i-eye"/></svg>VIEW</span><span class="icn"><svg width="14" height="10"><use href="#i-cloud"/></svg></span><span class="icn"><svg width="11" height="11"><use href="#i-link"/></svg></span></div></article>
    </div>
  </section>

  <section class="news-box">
    <div class="news">
      <div class="shelf-head"><span class="tab">LATEST NEWS</span>
        <div class="arrows"><i><svg width="6" height="8"><use href="#i-prev"/></svg></i><i><svg width="6" height="8"><use href="#i-next"/></svg></i></div></div>
      <article class="post"><div class="pic" role="img" aria-label="Photo of a dashboard on a laptop screen" style="background:linear-gradient(135deg,#e6edf3,#8fb8de 50%,#2f73b3)"></div>
        <div><h5>Request a Live Demo</h5><p>Short notes on new tools, smarter rotas and better coaching for busy floor teams today.</p></div></article>
      <article class="post"><div class="pic" role="img" aria-label="Photo of a team planning meeting" style="background:linear-gradient(135deg,#c9c2b4,#8a8376 50%,#4e4a44)"></div>
        <div><h5>What Makes a Successful Planning Team?</h5><p>Practical steps to plan staffing, forecast volume and keep every shift running on time.</p></div></article>
    </div>
    <aside class="about">
      <h4>About us</h4>
      <div class="name">Allphonedesk<br>Hub</div>
      <p>Our hub gathers courseware, templates, videos and research for call centre leaders. We help managers coach teams, lift service and grow skills with tools that are simple to use every day.</p>
      <span class="more">Know more</span>
    </aside>
  </section>
</main>

<footer class="footer">
  <div class="foot-cols">
    <div class="foot-col qc">
      <h4>QUICK CONTACT</h4>
      <div class="field">Name</div><div class="field">Email</div><div class="field area">Message</div>
      <div class="send">SUBMIT</div>
    </div>
    <div class="foot-col rc">
      <h4>RECENT COMMENT</h4>
      <div class="comment"><span class="avatar" role="img" aria-label="Member avatar"></span><span><b>Marco</b><br>Commented On 15 Dec 2015<br>Working good and nice</span></div>
      <div class="comment"><span class="avatar" role="img" aria-label="Member avatar"></span><span><b>Lena</b><br>Commented On 12 Dec 2015<br>Nice and good</span></div>
    </div>
    <div class="foot-col contact">
      <h4>CONTACT US</h4>
      <p><svg width="10" height="13" viewBox="0 0 10 13"><path d="M5 13S0 7 0 5a5 5 0 0110 0c0 2-5 8-5 8z" fill="#555"/><circle cx="5" cy="5" r="1.8" fill="#ececec"/></svg><span>88 Harbour Lane<br>Eastfield Park<br>Westbrook</span></p>
      <p><svg width="10" height="12" viewBox="0 0 14 14"><path d="M3 1l3 3-2 2c1 2 2 3 4 4l2-2 3 3-2 3C6 13 1 8 0 3z" fill="#555"/></svg><span>+44 555 0142</span></p>
      <p><svg width="12" height="9" viewBox="0 0 14 10"><rect width="14" height="10" fill="#555"/><path d="M1 1l6 5 6-5" fill="none" stroke="#ececec"/></svg><span>info@allphonedeskhub.net</span></p>
      <div class="squares"><i></i><i></i><i></i><i></i><i></i><i></i><i></i><i></i></div>
    </div>
  </div>
  <div class="copy">© Copyright 2015, Allphonedesk Hub</div>
</footer>

</div>
</body>
</html>
```